Solar Company Bussiness Card

I need a 2 sided business card and would like a .psd and any font files for each side of the card. I would like my logo used, it should be attached with the fonts. I'm not opposed to the font colors with the logo being changed.

On the sample design, I'd like the following:

Darren Pellow
President
Phone: 555-318-2947
www.sunvaleenergyco.example

As I've recently opened in a 2nd market, I'm not sure about an address as I currently have 2 of them. I may actually get separate cards printed, one batch for each address, that's why I need the PSD file.
Updates

I'm very pleased with the response and designs I've received here for my business card. First and foremost, I'd like to thank everyone who took the time to submit a design. There truly are a lot of great designs in the bunch here and I'm having a little difficulty deciding. I will be reaching out to someone in the next day or two here to go to a final design. At this time, I'm not looking for any new concepts. If any of you do logos, I'm looking for a new logo for our sister entity, Pellow Partners, Inc. Thanks, Darren Pellow

Reason: I'm not looking for any new designs at this point, but extending this deadline in order to give people I've asked a chance to re-submit items.

Industry/Entity Type

Business

```html
<!DOCTYPE html>
<html lang="en">
<head>
<meta charset="utf-8">
<title>Sunvale Energy – Business Card</title>
<link rel="stylesheet" href="https://fonts.googleapis.com/css2?family=Open+Sans:wght@400;600;700&display=swap">
<style>
  :root {
    --stage: #e9eaed;
    --card: #ffffff;
    --brand-blue: #1358a3;
    --ink: #2b2b2b;
    --ink-soft: #4a4a4a;
    --divider: #a9acb1;
  }
  * { box-sizing: border-box; margin: 0; padding: 0; }
  html, body { width: 1200px; height: 976px; overflow: hidden; }
  body {
    background: var(--stage);
    font-family: "Open Sans", Arial, sans-serif;
    color: var(--ink);
    position: relative;
  }
  .card {
    position: absolute;
    left: 220px;
    width: 760px;
    height: 434px;
    background: var(--card);
    border-radius: 26px;
    box-shadow: 0 6px 18px rgba(0,0,0,0.12);
    overflow: hidden;
  }
  .card--back { top: 36px; }
  .card--front { top: 506px; }

  .rule {
    position: absolute;
    left: 0; right: 0;
    height: 6px;
    background: var(--brand-blue);
  }
  .rule__marker {
    position: absolute;
    top: -7px;
    width: 20px; height: 20px;
    background: var(--brand-blue);
  }

  .brand {
    position: absolute;
    display: flex;
    align-items: center;
    gap: 14px;
    color: var(--brand-blue);
    font-weight: 600;
    letter-spacing: 0.5px;
    white-space: nowrap;
  }
  .brand__square {
    background: var(--brand-blue);
    flex: none;
  }

  /* back */
  .card--back .brand { left: 200px; top: 118px; font-size: 52px; }
  .card--back .brand__square { width: 42px; height: 42px; }
  .card--back .rule { top: 214px; }
  .card--back .rule__marker { left: 370px; }

  /* front */
  .card--front .brand { left: 48px; top: 48px; font-size: 36px; }
  .card--front .brand__square { width: 30px; height: 30px; }
  .card--front .rule { top: 232px; }
  .card--front .rule__marker { left: 300px; }

  .address {
    position: absolute;
    left: 48px; top: 300px;
    font-size: 20px;
    color: var(--ink-soft);
  }

  .contact {
    position: absolute;
    left: 470px; top: 60px;
    width: 270px;
    padding-left: 30px;
    border-left: 3px solid var(--divider);
  }
  .contact__name {
    font-size: 21px;
    font-weight: 700;
    letter-spacing: 0.5px;
    text-transform: uppercase;
  }
  .contact__title {
    font-size: 17px;
    color: var(--ink-soft);
    margin-top: 2px;
  }
  .contact__list {
    list-style: none;
    margin-top: 32px;
    font-size: 15px;
    color: var(--ink);
  }
  .contact__item {
    position: relative;
    line-height: 30px;
  }
  .contact__item::before {
    content: "";
    position: absolute;
    left: -40px; top: 8px;
    width: 14px; height: 14px;
    background: var(--brand-blue);
  }
</style>
</head>
<body>

  <section class="card card--back" aria-label="Business card back">
    <div class="brand"><span class="brand__square"></span>Sunvale Energy</div>
    <div class="rule"><span class="rule__marker"></span></div>
  </section>

  <section class="card card--front" aria-label="Business card front">
    <div class="brand"><span class="brand__square"></span>Sunvale Energy</div>
    <div class="rule"><span class="rule__marker"></span></div>
    <p class="address">24 Harbor Lane, Eastfield</p>

    <div class="contact">
      <p class="contact__name">Darren Pellow</p>
      <p class="contact__title">Managing Director</p>
      <ul class="contact__list">
        <li class="contact__item">555-318-2947</li>
        <li class="contact__item">555-402-7715</li>
        <li class="contact__item">darren@sunvaleenergyco.example</li>
        <li class="contact__item">www.sunvaleenergyco.example</li>
      </ul>
    </div>
  </section>

</body>
</html>
```